CareRally482
Business Cards and Stationary
CareRally482 - Emergency Services
Creative Brief
Use specific fonts
Use fonts and colors from our new logo and website that are attached
Professional
Gordon P. Hartwell
Owner
20415 E Ridge Ave Suite 230-519 Maple Ridge, NV 85261
gph@carerally482.com
www.carerally482.com
Use uploaded website draft for colors and fonts, you can get an idea of what we do from the current website. NOTE: We will need business card templates for; Marlena J. Hartwell Owner cell (623) 555-0187 email marlena@carerally482.com Douglas R. Pembry DO Medical Director cell (602)555-0134 email dpembrydo@carerally482.com
open to great ideas

```html
<!DOCTYPE html>
<html lang="en">
<head>
<meta charset="utf-8">
<title>CareRally482 Stationery</title>
<link href="https://fonts.googleapis.com/css2?family=Exo+2:wght@700&family=Open+Sans:wght@400;600&display=swap" rel="stylesheet">
<style>
  :root{
    --bg:#a9aaac;
    --paper:#ffffff;
    --blue:#2437a8;
    --blue-dark:#14207a;
    --blue-light:#4d6be0;
    --grey-text:#6d6e71;
    --grey-soft:#c9cacc;
    --ink:#3a3a3c;
    --faint:#eef0f6;
  }
  *{margin:0;padding:0;box-sizing:border-box}
  html,body{width:1200px;height:821px;overflow:hidden;background:var(--bg)}
  body{position:relative;font-family:"Open Sans",Arial,sans-serif;color:var(--ink)}
  .sheet{position:absolute;background:var(--paper);overflow:hidden;box-shadow:0 1px 3px rgba(0,0,0,.18)}
  .brand{position:absolute;display:flex;align-items:center;gap:6px;font-family:"Exo 2",Arial,sans-serif;font-weight:700;color:var(--grey-text);white-space:nowrap}
  .brand .dot{border-radius:50%;background:var(--blue);flex:none}
  .brand.on-blue{color:#fff}
  .brand.on-blue .dot{background:#fff}
  .watermark{position:absolute;display:flex;align-items:center;gap:12px;font-family:"Exo 2",Arial,sans-serif;font-weight:700;color:var(--faint);white-space:nowrap}
  .watermark .ring{border-radius:50%;border:9px solid var(--faint);flex:none}
  .contact{position:absolute;font-size:6.5px;line-height:9.6px;color:var(--ink)}
  .contact li{list-style:none;display:flex;align-items:center;gap:4px}
  .contact li i{display:inline-block;width:5px;height:5px;border-radius:50%;background:var(--blue);flex:none}
  .swoosh{position:absolute;left:0;bottom:0;width:100%}

  .letterhead{left:29px;top:29px;width:537px;height:768px}
  .card{width:222px;height:125px}
  .card-back{left:941px;top:43px;width:230px}
  .card-white{left:667px;top:187px;background:linear-gradient(#fff,#e8e9eb)}
  .card-blue{left:902px;top:187px;width:269px;background:radial-gradient(ellipse at 40% 40%,var(--blue-light),var(--blue) 55%,var(--blue-dark))}
  .card-name{position:absolute;right:10px;top:9px;text-align:right;color:#fff;line-height:1.25}
  .card-name strong{display:block;font-size:9px;font-weight:600}
  .card-name span{font-size:6px}
  .card-web{position:absolute;left:0;right:0;bottom:14px;text-align:center;font-size:5.5px;color:var(--grey-text)}
  .envelope{left:583px;top:408px;width:588px;height:384px}
</style>
</head>
<body>

<section class="sheet letterhead">
  <div class="brand" style="left:26px;top:34px;font-size:25px"><span>CareRally482</span><span class="dot" style="width:24px;height:24px"></span></div>
  <ul class="contact" style="left:427px;top:14px">
    <li>20415 E Ridge Ave Suite 230-519</li>
    <li>Maple Ridge, NV 85261</li>
    <li><i></i>Ph (623) 555-0187</li>
    <li><i></i>Cell (730) 555-0188</li>
    <li><i></i>Alt (730) 555-0189</li>
    <li><i></i>Fax (888) 555-0176</li>
    <li><i></i>gph@carerally482.com</li>
    <li><i></i>www.carerally482.com</li>
  </ul>
  <div class="watermark" style="left:40px;top:300px;font-size:44px"><span class="ring" style="width:130px;height:130px"></span><span>CareRally482</span></div>
  <svg class="swoosh" viewBox="0 0 537 120" height="120" preserveAspectRatio="none">
    <defs><linearGradient id="lhBlue" x1="0" y1="0" x2="1" y2="0"><stop offset="0" stop-color="#4d6be0"/><stop offset="1" stop-color="#1c2a92"/></linearGradient></defs>
    <path d="M0 14 C180 48 360 44 537 28 L537 48 C360 66 180 66 0 32Z" fill="var(--grey-soft)"/>
    <path d="M0 42 C180 74 360 70 537 52 L537 120 L0 120Z" fill="url(#lhBlue)"/>
  </svg>
</section>

<section class="sheet card card-back">
  <svg width="230" height="125" viewBox="0 0 230 125" style="position:absolute;left:0;top:0">
    <defs><linearGradient id="cbBlue" x1="0" y1="0" x2="1" y2="1"><stop offset="0" stop-color="#4d6be0"/><stop offset="1" stop-color="#14207a"/></linearGradient></defs>
    <path d="M0 0 H230 V125 H190 C170 90 175 50 230 42 L230 38 C140 44 60 40 0 32Z" fill="url(#cbBlue)"/>
  </svg>
  <div class="card-name"><strong>Gordon P. Hartwell</strong><span>Owner</span></div>
  <ul class="contact" style="left:104px;top:48px;font-size:5.5px;line-height:8px">
    <li>20415 E Ridge Ave Suite 230-519</li>
    <li>Maple Ridge, NV 85261</li>
    <li><i></i>(623) 555-0187</li>
    <li><i></i>(888) 555-0176</li>
    <li><i></i>gph@carerally482.com</li>
    <li><i></i>www.carerally482.com</li>
  </ul>
</section>

<section class="sheet card card-white">
  <div class="brand" style="left:30px;top:48px;font-size:21px"><span>CareRally482</span><span class="dot" style="width:20px;height:20px"></span></div>
  <p class="card-web">www.carerally482.com</p>
</section>

<section class="sheet card card-blue">
  <div class="brand on-blue" style="left:42px;top:48px;font-size:23px"><span>CareRally482</span><span class="dot" style="width:20px;height:20px"></span></div>
</section>

<section class="sheet envelope">
  <svg width="588" height="384" viewBox="0 0 588 384" style="position:absolute;left:0;top:0">
    <defs>
      <linearGradient id="flap" x1="0" y1="0" x2="0" y2="1"><stop offset="0" stop-color="#14207a"/><stop offset="1" stop-color="#3d5ad4"/></linearGradient>
      <linearGradient id="envBlue" x1="0" y1="0" x2="1" y2="0"><stop offset="0" stop-color="#4d6be0"/><stop offset="1" stop-color="#1c2a92"/></linearGradient>
    </defs>
    <path d="M0 0 H588 V60 C420 118 168 118 0 60Z" fill="url(#flap)"/>
    <path d="M0 60 C168 118 420 118 588 60 L588 66 C420 124 168 124 0 66Z" fill="#8fa0e6" opacity=".6"/>
    <path d="M0 320 C200 346 400 344 588 318 L588 332 C400 356 200 356 0 332Z" fill="var(--grey-soft)"/>
    <path d="M0 336 C200 360 400 358 588 334 L588 384 L0 384Z" fill="url(#envBlue)"/>
  </svg>
  <div class="brand on-blue" style="left:238px;top:30px;font-size:15px"><span>CareRally482</span><span class="dot" style="width:14px;height:14px"></span></div>
  <div class="watermark" style="left:290px;top:180px;font-size:26px"><span class="ring" style="width:84px;height:84px;border-width:6px"></span><span>CareRally482</span></div>
  <div class="brand" style="left:14px;top:160px;font-size:22px"><span>CareRally482</span><span class="dot" style="width:20px;height:20px"></span></div>
  <ul class="contact" style="left:14px;top:198px">
    <li>20415 E Ridge Ave Suite 230-519</li>
    <li>Maple Ridge, NV 85261</li>
    <li><i></i>Ph (623) 555-0187</li>
    <li><i></i>Cell (730) 555-0188</li>
    <li><i></i>Alt (730) 555-0189</li>
    <li><i></i>Fax (888) 555-0176</li>
    <li><i></i>gph@carerally482.com</li>
    <li><i></i>www.carerally482.com</li>
  </ul>
</section>

</body>
</html>
```